New website for an SEO training system

We need a web design for an SEO company offering a Rank Ladder Kit product which is a system or recipe on how to do SEO on your blog. It's a bit like, "28 Mornings for Sharper Writing Habits" in that they it is chunked down to what should be done on a daily basis over a 30 day period. It's not so much a training product but a recipe book.
The materials are video and support docs, like to do lists and checklists. It needs to be fresh and clean, with modern design.

Target Market(s)

Bloggers

Industry/Entity Type

It Company

Font styles to use
Sans Serif

```html
<!DOCTYPE html>
<html lang="en">
<head>
<meta charset="utf-8">
<title>RankLadder – Rank Ladder Kit</title>
<link rel="stylesheet" href="https://fonts.googleapis.com/css2?family=Lato:wght@400;700;900&display=swap">
<style>
:root{
  --dark:#3a3a3a;
  --darker:#2c2c2c;
  --orange:#f39a1e;
  --green:#4cc13a;
  --green-dark:#3aa52b;
  --teal:#1ea7d9;
  --navy:#1f3b63;
  --text:#333;
  --muted:#777;
  --line:#d9d9d9;
  --panel:#eeeeec;
  --white:#fff;
}
*{box-sizing:border-box;margin:0;padding:0}
html,body{width:766px;height:1200px;overflow:hidden}
body{font-family:'Lato',sans-serif;color:var(--text);background:var(--white);position:relative}
.site-header{height:78px;background:var(--dark);position:relative}
.brand{position:absolute;left:36px;top:22px;display:flex;align-items:center;gap:10px;color:var(--white);font-weight:900;font-size:28px;letter-spacing:.5px}
.brand-mark{width:14px;height:14px;background:var(--orange)}
.social{position:absolute;right:36px;top:12px;display:flex;gap:6px}
.social span{width:14px;height:14px;border-radius:50%;border:1.5px solid #bbb}
.main-nav{position:absolute;right:36px;top:46px;display:flex;gap:24px}
.main-nav a{color:var(--white);text-decoration:none;font-size:15px;font-weight:700;letter-spacing:.4px}
.hero{position:relative;height:240px}
.benefits{position:absolute;left:46px;top:20px;list-style:none}
.benefits li{display:flex;align-items:center;gap:12px;color:var(--orange);font-weight:900;font-size:21px;height:37px}
.benefits svg{width:22px;height:22px}
.video{position:absolute;right:36px;top:12px;width:352px;height:206px;background:#161616;border:3px solid #0d0d0d}
.video-title{position:absolute;top:50px;width:100%;text-align:center;color:var(--white);font-weight:900;font-size:30px;letter-spacing:1px}
.video-play{position:absolute;left:152px;top:100px}
.video-bar{position:absolute;left:0;right:0;bottom:0;height:24px;background:#2a2a2a;display:flex;align-items:center;padding:0 10px;gap:10px}
.video-track{flex:1;height:5px;background:#555;border-radius:3px}
.video-track i{display:block;width:18%;height:100%;background:#aaa;border-radius:3px}
.rule{height:1px;background:var(--line);margin:0 36px}
.section-title{text-align:center;font-size:31px;font-weight:700;color:var(--text)}
.stories{padding-top:22px;height:258px}
.story-list{display:flex;justify-content:center;gap:92px;margin-top:16px}
.story{width:140px;text-align:center}
.story-photo{width:88px;height:88px;border-radius:50%;margin:0 auto;background:radial-gradient(circle at 50% 40%,#c9b8a6,#5b6b80);border:3px solid #eee}
.story h3{font-size:21px;font-weight:700;margin:8px 0 4px}
.story p{font-size:10px;line-height:1.4;color:var(--muted)}
.services{padding-top:24px;height:270px}
.service-grid{display:grid;grid-template-columns:1fr 1fr;column-gap:40px;row-gap:24px;margin:24px 50px 0 50px}
.service{display:flex;gap:16px}
.service svg{flex:none;width:46px;height:46px}
.service h3{font-size:18px;font-weight:700;margin-bottom:4px}
.service p{font-size:10px;line-height:1.45;color:var(--muted)}
.guarantee{margin:14px 36px 0;height:150px;background:var(--panel);border:1px solid #ddd;position:relative;display:flex;padding:26px 24px 0 162px}
.guarantee-label{position:absolute;left:18px;top:-12px;background:var(--orange);color:var(--white);font-weight:900;font-size:17px;padding:3px 12px;letter-spacing:.5px}
.guarantee-seal{position:absolute;left:40px;top:30px;width:86px;height:100px;border-radius:43px 43px 8px 8px;background:linear-gradient(#f4c431,#d9541d)}
.guarantee p{font-size:12px;line-height:1.33;color:#555}
.cta-wrap{text-align:center;margin-top:30px}
.cta{display:inline-block;width:220px;height:58px;line-height:54px;background:var(--green);border-bottom:4px solid var(--green-dark);color:var(--white);font-weight:900;font-size:19px;text-decoration:none;letter-spacing:.5px}
.site-footer{position:absolute;left:0;right:0;bottom:0;height:40px;background:var(--darker);color:#aaa;font-size:10px;display:flex;align-items:center;justify-content:center;gap:6px}
.site-footer a{color:var(--orange);text-decoration:none}
</style>
</head>
<body>
<header class="site-header">
  <div class="brand"><span class="brand-mark"></span>RANKLADDER</div>
  <div class="social"><span></span><span></span><span></span></div>
  <nav class="main-nav"><a href="#">HOME</a><a href="#">SUCCESS STORIES</a><a href="#">FAQs</a><a href="#">BLOG</a><a href="#">LOGIN</a></nav>
</header>

<section class="hero">
  <ul class="benefits">
    <li><svg viewBox="0 0 24 24"><path d="M3 13l6 6L21 5" fill="none" stroke="#4cc13a" stroke-width="4"/></svg>Create Sales Pages</li>
    <li><svg viewBox="0 0 24 24"><path d="M3 13l6 6L21 5" fill="none" stroke="#4cc13a" stroke-width="4"/></svg>Converting Landing Pages</li>
    <li><svg viewBox="0 0 24 24"><path d="M3 13l6 6L21 5" fill="none" stroke="#4cc13a" stroke-width="4"/></svg>Membership Portals</li>
    <li><svg viewBox="0 0 24 24"><path d="M3 13l6 6L21 5" fill="none" stroke="#4cc13a" stroke-width="4"/></svg>Complete Launch Funnels</li>
    <li><svg viewBox="0 0 24 24"><path d="M3 13l6 6L21 5" fill="none" stroke="#4cc13a" stroke-width="4"/></svg>Authority Blog Sites</li>
  </ul>
  <div class="video">
    <div class="video-title">RANKLADDER</div>
    <svg class="video-play" width="42" height="42" viewBox="0 0 42 42"><circle cx="21" cy="21" r="20" fill="rgba(255,255,255,.35)"/><path d="M16 12l14 9-14 9z" fill="#fff"/></svg>
    <div class="video-bar">
      <svg width="10" height="12" viewBox="0 0 10 12"><path d="M0 0l10 6-10 6z" fill="#ddd"/></svg>
      <div class="video-track"><i></i></div>
      <svg width="14" height="12" viewBox="0 0 14 12"><path d="M0 4h4l5-4v12l-5-4H0z" fill="#ddd"/></svg>
    </div>
  </div>
</section>

<div class="rule"></div>

<section class="stories">
  <h2 class="section-title">Success stories</h2>
  <div class="story-list">
    <article class="story"><div class="story-photo" role="img" aria-label="Portrait photo of James"></div><h3>james story</h3><p>Donec nec elit venenatis turpis dapibus gravida. Ut ornare ipsum ut ante ullamcorper, eget gravida nulla mattis.</p></article>
    <article class="story"><div class="story-photo" role="img" aria-label="Portrait photo of Leo"></div><h3>leo story</h3><p>Donec nec elit venenatis turpis dapibus gravida. Ut ornare ipsum ut ante ullamcorper, eget gravida nulla mattis.</p></article>
    <article class="story"><div class="story-photo" role="img" aria-label="Portrait photo of Linda"></div><h3>linda story</h3><p>Donec nec elit venenatis turpis dapibus gravida. Ut ornare ipsum ut ante ullamcorper, eget gravida nulla mattis.</p></article>
  </div>
</section>

<div class="rule"></div>

<section class="services">
  <h2 class="section-title">What we can do for you</h2>
  <div class="service-grid">
    <div class="service">
      <svg viewBox="0 0 46 46"><circle cx="23" cy="23" r="23" fill="var(--teal)"/><rect x="12" y="14" width="22" height="15" fill="none" stroke="#fff" stroke-width="2.5"/><path d="M18 34h10M23 29v5" stroke="#fff" stroke-width="2.5"/></svg>
      <div><h3>Landing pages</h3><p>Lorem ipsum dolor sit amet, consectetur adipiscing elit. Phasellus placerat gravida orci, non accumsan diam dignissim in.</p></div>
    </div>
    <div class="service">
      <svg viewBox="0 0 46 46"><rect width="46" height="46" fill="var(--navy)"/><path d="M23 10l11 4v8c0 7-5 12-11 14-6-2-11-7-11-14v-8z" fill="#fff"/></svg>
      <div><h3>Secure Membership Portals</h3><p>Lorem ipsum dolor sit amet, consectetur adipiscing elit. Phasellus placerat gravida orci, non accumsan diam dignissim in.</p></div>
    </div>
    <div class="service">
      <svg viewBox="0 0 46 46"><circle cx="23" cy="23" r="23" fill="var(--teal)"/><path d="M11 14h4l3 13h14l3-9H17" fill="none" stroke="#fff" stroke-width="2.5"/><circle cx="20" cy="32" r="2" fill="#fff"/><circle cx="30" cy="32" r="2" fill="#fff"/></svg>
      <div><h3>Sales &amp; Marketing</h3><p>Lorem ipsum dolor sit amet, consectetur adipiscing elit. Phasellus placerat gravida orci, non accumsan diam dignissim in.</p></div>
    </div>
    <div class="service">
      <svg viewBox="0 0 46 46"><rect width="46" height="46" fill="var(--navy)"/><path d="M23 8c5 4 6 10 5 18h-10c-1-8 0-14 5-18z" fill="#fff"/><path d="M18 22l-5 7h5zM28 22l5 7h-5zM20 30l3 7 3-7z" fill="#fff"/></svg>
      <div><h3>Product Launch Funnels</h3><p>Lorem ipsum dolor sit amet, consectetur adipiscing elit. Phasellus placerat gravida orci, non accumsan diam dignissim in.</p></div>
    </div>
  </div>
</section>

<section class="guarantee">
  <span class="guarantee-label">GUARANTEE</span>
  <div class="guarantee-seal" role="img" aria-label="Guarantee seal with ribbon"></div>
  <p>Lorem ipsum dolor sit amet, consectetur adipiscing elit. Phasellus placerat gravida orci, non accumsan diam dignissim in. Cras dapibus in leo at porttitor. Pellentesque id ipsum tincidunt, auctor leo ut, pharetra eros. Fusce bibendum faucibus risus, nec aliquam arcu varius at. Curabitur efficitur eu ex euismod interdum. Suspendisse lorem nibh, pulvinar vitae porta id, tincidunt a turpis. Praesent leo risus, interdum a metus sed, consectetur viverra nunc. Suspendisse potenti. Suspendisse potenti. Suspendisse lorem nibh, pulvinar vitae porta id, tincidunt a turpis. Praesent leo risus, interdum a metus sed, consectetur.</p>
</section>

<div class="cta-wrap"><a class="cta" href="#">GET STARTED NOW</a></div>

<footer class="site-footer">© www.example.com 2013 | <a href="#">Privacy Policy</a> | <a href="#">Terms of Service</a> | <a href="#">Site Map</a></footer>
</body>
</html>
```